Brightfield Optics seeks updated contemporary business card

Brightfield Optics utilizes advanced technology and we take pride in the modern look and feel of our practice. We like our current card, but it's been four years so it is time for an update.

Target Market(s)

Females 25-45 make the most health care decisions for their family.

Contact Information for Business Card

Clean front. Back with info and with empty space for appointment time or other small note

Requirements
Must have
• Logo
Ridge Marketvale, 28413 E Larkspur Ave
Cedar Terrace Marketvale, 4638 S Dunmore Rd
Call or text: 509-342-1968
email: hello@brightfieldoptics.example
brightfieldoptics.example
Dr Tobias Werring & Associates

```html
<!DOCTYPE html>
<html lang="en">
<head>
<meta charset="utf-8">
<title>Brightfield Optics – Business Card</title>
<link rel="stylesheet" href="https://fonts.googleapis.com/css2?family=Open+Sans:wght@600;700;800&display=swap">
<style>
  :root {
    --backdrop: #e8e5e0;
    --card-grey: #6b6e71;
    --panel-white: #f4f4f4;
    --brand-blue: #1a7fc1;
    --ribbon-fold: #0f5a8c;
    --icon-blue: #2aa1de;
    --brand-navy: #232f5e;
    --text-light: #f2f2f2;
  }
  * { margin: 0; padding: 0; box-sizing: border-box; }
  html, body {
    width: 1200px; height: 900px; overflow: hidden;
    background: var(--backdrop);
    font-family: "Open Sans", sans-serif;
  }
  .canvas {
    position: relative; width: 1200px; height: 900px;
    display: flex; flex-direction: column; align-items: center; justify-content: center; gap: 40px;
  }
  .card {
    width: 700px; height: 400px; display: block;
    box-shadow: 0 10px 24px rgba(0,0,0,0.22);
  }
  .card-name { font-weight: 800; font-size: 18px; fill: #ffffff; letter-spacing: 0.3px; }
  .card-detail { font-weight: 700; font-size: 12px; fill: var(--text-light); letter-spacing: 0.4px; }
  .card-phone { font-weight: 800; font-size: 18px; fill: var(--text-light); letter-spacing: 1px; }
  .brand-name { font-weight: 800; fill: var(--brand-navy); }
</style>
</head>
<body>
<main class="canvas">

  <!-- Info side -->
  <svg class="card card-back" viewBox="0 0 700 400" aria-label="Business card, contact side">
    <rect class="card-base" width="700" height="400" fill="var(--card-grey)"/>
    <path class="brand-panel" d="M0,40 H320 A360 360 0 0 0 320,360 H0 Z" fill="var(--panel-white)"/>

    <g class="brand-lockup">
      <circle cx="36" cy="198" r="9" fill="var(--brand-blue)"/>
      <text class="brand-name" x="54" y="206" font-size="22">Brightfield Optics</text>
    </g>

    <g class="name-ribbon">
      <polygon points="285,94 301,104 301,94" fill="var(--ribbon-fold)"/>
      <polygon points="285,60 700,40 700,76 285,94" fill="var(--brand-blue)"/>
      <rect x="306" y="64" width="26" height="24" rx="4" fill="var(--icon-blue)"/>
      <circle cx="319" cy="73" r="4.5" fill="#ffffff"/>
      <path d="M311,85 a8,6 0 0 1 16,0 Z" fill="#ffffff"/>
      <text class="card-name" x="344" y="83">Dr Tobias Werring &amp; Associates</text>
    </g>

    <g class="contact-address">
      <rect x="330" y="128" width="26" height="24" rx="4" fill="var(--icon-blue)"/>
      <path d="M343,133 a5.5,5.5 0 0 1 5.5,5.5 c0,4 -5.5,9 -5.5,9 c0,0 -5.5,-5 -5.5,-9 a5.5,5.5 0 0 1 5.5,-5.5 Z" fill="#ffffff"/>
      <circle cx="343" cy="138.5" r="2" fill="var(--icon-blue)"/>
      <text class="card-detail" x="368" y="131">Ridge Marketvale, 28413 E Larkspur Ave</text>
      <text class="card-detail" x="368" y="153">Cedar Terrace Marketvale, 4638 S Dunmore Rd</text>
    </g>

    <g class="contact-email">
      <rect x="330" y="188" width="26" height="24" rx="4" fill="var(--icon-blue)"/>
      <rect x="335" y="194" width="16" height="11" fill="#ffffff"/>
      <path d="M335,194 L343,201 L351,194" fill="none" stroke="var(--icon-blue)" stroke-width="1.5"/>
      <text class="card-detail" x="368" y="205">hello@brightfieldoptics.example</text>
    </g>

    <g class="contact-web">
      <rect x="330" y="236" width="26" height="24" rx="4" fill="var(--icon-blue)"/>
      <circle cx="343" cy="248" r="7" fill="none" stroke="#ffffff" stroke-width="1.4"/>
      <ellipse cx="343" cy="248" rx="3" ry="7" fill="none" stroke="#ffffff" stroke-width="1.2"/>
      <line x1="336" y1="248" x2="350" y2="248" stroke="#ffffff" stroke-width="1.2"/>
      <text class="card-detail" x="368" y="253">brightfieldoptics.example</text>
    </g>

    <g class="contact-phone">
      <rect x="330" y="284" width="26" height="24" rx="4" fill="var(--icon-blue)"/>
      <path d="M337,289 l4,0 l1.5,4 l-2.5,1.5 a10,10 0 0 0 5,5 l1.5,-2.5 l4,1.5 l0,4 a2,2 0 0 1 -2,2 a14,14 0 0 1 -13.5,-13.5 a2,2 0 0 1 2,-2 Z" fill="#ffffff"/>
      <text class="card-phone" x="368" y="303">509-342-1968</text>
    </g>
  </svg>

  <!-- Clean side -->
  <svg class="card card-front" viewBox="0 0 700 400" aria-label="Business card, brand side">
    <rect class="card-base" width="700" height="400" fill="var(--card-grey)"/>
    <circle class="brand-disc" cx="350" cy="200" r="150" fill="var(--panel-white)" stroke="var(--brand-blue)" stroke-width="5"/>
    <text class="brand-name" x="350" y="211" font-size="28" text-anchor="middle">Brightfield Optics</text>
  </svg>

</main>
</body>
</html>
```